Zelmor Africa - Website Design Brief

Web Design Brief

ZELMOR AFRICA
WEBSITE DESIGN BRIEF

INTRODUCTION
ABOUT ZELMOR
• ZELMOR is a premier consulting firm that specialises in aiding global corporations and emerging businesses to enter and scale within Africa's dynamic markets. Through swift, actionable insights and innovative strategies, ZELMOR empowers clients to capitalise on Africa's untapped potential, thereby catering specifically to forward-thinking entities poised for exponential growth.

TASK DESCRIPTION
• Develop a 5-page website for ZELMOR.
• The primary goal is to present a clear and concise picture of our consulting firm, its Africa-centric experience, and its offerings to multinational clients looking for a professional partner to penetrate African markets or reclaim lost market share.

WEBSITE FRAMEWORK
Page Architecture:
• Home
o A powerful landing page that instantly communicates who ZELMOR is and what solutions it provides. Incorporate impactful visuals and calls-to-action.
• About
o A compelling narrative that illustrates ZELMOR's unique approach to consulting, dedication to Africa, and experience assisting multinational firms.
• Services
o A showcase of ZELMOR's successful projects and client testimonials. This page should build trust and credibility, demonstrating ZELMOR's ability to deliver exceptional results.
• Team
o Introduce up to 8 key team members, with each profile featuring a professional photo, name, title, and a brief bio showcasing the individual's skills, experiences, and contributions to ZELMOR's mission.
• Contact
o Clear and easy ways for visitors to contact ZELMOR for more information or to initiate a partnership.
• Footer
o Links to ZELMOR's social media profiles on Instagram and LinkedIn, along with a privacy policy.
o Social links
o Instagram: https://www.instagram.com/zelmorafrica/
o LinkedIn: https://www.linkedin.com/company/zelmorafrica/
o Privacy Policy
o Insert placeholder "lorem ipsum" text.
o Text will be provided with the revision round or ZELMOR will update text on site handover.

DESIGN INSPIRATION
• The website's design should evoke professionalism and elegance, with simple and clean lines inspired by site pages like:
o https://quendaro.example/
o https://quendaro.example/services/
o One aspect we particularly appreciate is how visitors can easily navigate by scrolling down to find what they're looking for and see everything they need to in an intuitive way on the home page
o What we don’t like about this site is how they navigate from the home page to other random pages – we like about to take you to the about page, and so on.

Branding Guidelines:
• See logo on Pixel Bazaar: Design #: 58170926
• We like the idea of the logo being black or white and have uploaded these options as well.
• Monochrome themes, with spots or splash of colour to highlight something is a style we appreciate.

Website Objectives and Goals:
• Our website's primary goal is to create a strong online presence, acting as a hub for potential clients to discover our credibility, reliability, and our ability to deliver exceptional results. It's essential that our website portrays professionalism, instils trustworthiness, and showcases our sincere dedication to Africa.

Target audience:
• ZELMOR's audience consists of businesses in mobile money, gaming, FMCG, beverage, and alcohol sectors, primarily Business Development Managers or Operations Managers who are seeking insight into their respective marketplaces.

Company Overview:
• ZELMOR stands out from the crowd as a consulting firm with a difference. Our dynamic team is fully dedicated to one mission: brand development within Africa.
• Unlike other companies that focus solely on online connectivity, we recognize the tremendous value in embracing the vibrant street culture that makes Africa so unique. Community engagement, empowerment, and expansion are at the forefront of everything we do.
• we recognize that unlocking business growth starts with a deep understanding of consumer behavior. It is this understanding that bridges the gap between companies and the communities that drive the cash economy. Our purpose is to reconnect businesses with the vibrant pulse of these essential local markets, injecting fresh vitality into their brands and propelling them towards resounding success in Africa.

Development to include:
• Basic SEO Setup:
o The website should be optimized for search engines, incorporating keywords, meta tags, and alt tags for images.
• Google Analytics Setup.
o To track website traffic and user behaviour for ongoing optimization.
• Google Crawling Setup
o The website needs to be easily indexed by Google, allowing it to appear in search results, and updated information effectively crawled by Google SEO and AHREFS scores.

PAGE CONTENT:
Home Page
• Background
o Option #1
o 4K video on home page, running on loop
o Bold Statement Text over Video
o Option #2
o Still Image
o Animated text making bold statement (e.g. our motto)

• Sections
o Contrast colour blocks or a way of making it clear that the next topic is a new topic.
o 5 sections
1. Home Main - Video + bold statement text
2. About - A paragraph and visual about us (lorem ipsum) that has a click through to our About Page (ignore how quendaro.example navigate, we think this is too complicated for our needs)
3. Services – communicated in some simple and powerful ways (we leave this open to you) – but keeping in mind it needs to be concise and professional.
4. Other - Something about our process that makes us unique (lorem ipsum text) and a placeholder image/animation.
5. Contact – a call-to-action button that takes you to our contact, but showcases a mobile number and email address.
6. Footer – as described in the previous section – placeholder for Instagram and LinkedIn only.

About Page
• Don’t reference quendaro.example for this page.
• Main Section
o Bold statements and images
• History Section
o A story about us and our past
• Final Section
o Some of our comments and final thoughts

Services Page
• How https://quendaro.example/services/ is laid out is great – we prefer a light theme.
• 6 - 8 x icons with headings and a brief description text box, and a read more drop down – all as placeholders to be edited later.
• For ease of direction for this page, look to the link shared above.

Team
• Add Placeholders for up to 8 team members (we only have 4 now):
o Image placeholder
o Name placeholder
o Title placeholder
o Short Bio (lorem ipsum)

Contact
• Clear and easy ways for visitors to contact ZELMOR for more information or to initiate a partnership.

• Insert placeholder "lorem ipsum" text, we will provide the text with our revision round.
o Ideally an easy form process that gives the user some options or dropdowns to complete before submission – up to 3 would be sufficient.
o Require their name and contact details.

NOTE: Images to follow:

Target Market(s)

ZELMOR's audience consists of businesses in mobile money, gaming, FMCG, beverage, and alcohol sectors, primarily Business Development Managers or Operations Managers who are seeking insight into their respective marketplaces.

Industry/Entity Type

ZELMOR is a premier consulting firm that specialises in aiding global corporations and emerging businesses to enter and scale within Africa's dynamic markets

Coding

Coded - Design and coding required

Number of Pages Required

5+ page

Font styles to use
Sans Serif
Other font styles liked:
• Poppins Font Family

Colors

Designer to choose colors to be used in the design.

Requirements
Must have
• The primary goal is to present a clear and concise picture of our consulting firm, and it's specialisation in Africa - smooth and crisp UI with animations or transitions that imply we know our way around tecchnology is always helpful - but a Clean and responsive UI is most important.
Nice to have
• Reactive and animated transitions through sections or pages - not overdone - adds a professional feel to the site
Should not have
• We don't want too many colours, and we don't want it too dark - we want a monochrome theme, with accents of colour when relevant

```html
<!DOCTYPE html>
<html lang="en">
<head>
<meta charset="utf-8">
<title>ZELMOR — Website Design</title>
<link href="https://fonts.googleapis.com/css2?family=Inter:wght@300;400;500;600;700&display=swap" rel="stylesheet">
<style>
:root{
  --blue:#0170bb;
  --ink:#1e1e1e;
  --paper:#f0f1f2;
  --board:#e6eaed;
  --black:#111111;
  --card:#1e1e1e;
  --muted:#7b7f84;
  --font:"Inter", sans-serif;
}
*{margin:0;padding:0;box-sizing:border-box}
html,body{width:1200px;height:2287px;overflow:hidden}
body{background:var(--board);font-family:var(--font);color:var(--ink);position:relative}
.abs{position:absolute}

/* brand header */
.brand-logo{left:203px;top:131px;color:var(--blue);font-weight:600;font-size:38px;letter-spacing:1px;line-height:40px}
.fonts-title{left:597px;top:100px;font-size:27px;font-weight:400}
.fonts-name{left:597px;top:150px;font-size:15px;color:var(--muted)}
.colors-title{left:889px;top:100px;font-size:27px;font-weight:400}
.swatch{top:138px;width:41px;height:41px;border-radius:50%}
.swatch-label{top:187px;font-size:9px;color:#555;width:52px;text-align:center}

/* site */
.site{left:222px;top:272px;width:792px;height:1911px;background:var(--paper);overflow:hidden}
.site *{position:absolute}

.hero{left:0;top:0;width:792px;height:439px;background:linear-gradient(135deg,#3a3a3a,#5c5c5c 45%,#2b2b2b)}
.nav-line{left:0;top:45px;width:792px;height:1px;background:rgba(255,255,255,.15)}
.nav-logo{left:107px;top:14px;color:#fff;font-weight:600;font-size:16px;line-height:18px}
.nav-link{top:18px;font-size:8px;color:#fff}
.btn-blue{left:622px;top:11px;width:63px;height:24px;background:var(--blue);color:#fff;font-size:7.5px;font-weight:600;display:flex;align-items:center;justify-content:center}
.hero-quote{left:404px;top:133px;width:278px;font-size:8.4px;line-height:14.8px;color:#fff;font-weight:300;padding-left:6px;border-left:2px solid var(--blue)}
.hero-title{left:105px;top:314px;font-size:30px;line-height:34px;font-weight:700;color:#fff;white-space:nowrap}
.hero-title .accent,.text-accent{position:static;color:var(--blue)}

.map{left:160px;top:496px;width:80px;height:110px;background:radial-gradient(ellipse,#dfe2e5 0%,rgba(223,226,229,0) 70%)}
.stat-num{top:490px;font-size:44px;font-weight:300;color:var(--ink);line-height:50px}
.stat-label{top:544px;font-size:8.5px;color:var(--muted);white-space:nowrap}
.intro{left:404px;top:492px;width:300px;font-size:18.4px;line-height:23.8px;color:var(--ink)}

.about{left:0;top:666px;width:792px;height:449px;background:var(--black)}
.eyebrow{font-size:6.5px;letter-spacing:2.4px;text-transform:uppercase}
.about .eyebrow{left:109px;top:56px;color:#aaa}
.section-title{font-size:23.5px;line-height:26px;font-weight:600;white-space:nowrap}
.about .section-title{left:107px;top:70px;color:#fff}
.about-card{left:107px;top:146px;width:578px;height:246px;background:var(--card);border-radius:3px}
.photo{border-radius:1px}
.about-text{left:30px;top:142px;width:270px;font-size:8.6px;line-height:13.9px;color:#cfd2d5;font-weight:300}
.about-text b{position:static;color:#fff;font-weight:500}
.read-light{left:29px;top:206px;font-size:7.5px;color:#fff;font-weight:500;text-decoration:underline}

.services{left:0;top:1115px;width:792px;height:298px}
.services .eyebrow{left:107px;top:57px;color:#888}
.services .section-title{left:107px;top:68px;color:var(--ink)}
.service{top:120px;width:130px}
.service svg{position:static;display:block;width:36px;height:36px}
.service-title{position:static!important;margin-top:12px;font-size:10px;font-weight:500;white-space:nowrap}
.service-desc{position:static!important;margin-top:8px;font-size:7.3px;line-height:12.6px;color:var(--muted)}
.service-link{position:static!important;margin-top:6px;font-size:7.3px;color:var(--blue)}

.process{left:0;top:1413px;width:792px;height:265px;background:var(--blue)}
.process .eyebrow{left:107px;top:56px;color:#cfe3f3}
.process .section-title{left:107px;top:68px;color:#fff}
.step{top:128px;width:150px;color:#fff}
.step-title{position:static!important;font-size:9.5px;font-weight:600}
.step-dot{position:static!important;display:block;width:9px;height:9px;border-radius:50%;background:#fff;margin-top:12px}
.step-desc{position:static!important;margin-top:10px;font-size:7.4px;line-height:12.9px;color:#d9e9f6}

.cta{left:0;top:1678px;width:792px;height:109px;background:var(--black);border-bottom:1px solid #2a2a2a}
.cta-title{left:107px;top:55px;font-size:24px;font-weight:500;color:#fff;white-space:nowrap}
.btn-outline{left:610px;top:57px;width:75px;height:28px;border:1px solid var(--blue);color:#fff;font-size:7.5px;font-weight:600;display:flex;align-items:center;justify-content:center}

.footer{left:0;top:1787px;width:792px;height:124px;background:var(--black)}
.copyright{left:107px;top:58px;font-size:6.5px;color:#aaa}
.foot-head{top:24px;font-size:9.5px;font-weight:600;color:#fff;white-space:nowrap}
.foot-link{font-size:6.8px;color:#aaa;white-space:nowrap}
.social{top:48px;width:16px;height:16px;border-radius:50%;background:#3a3a3a}
</style>
</head>
<body>

<header>
  <div class="abs brand-logo">ZELMOR</div>
  <div class="abs fonts-title">Fonts</div>
  <div class="abs fonts-name">Halvern Sans</div>
  <div class="abs colors-title">Colors:</div>
  <div class="abs swatch" style="left:890px;background:var(--blue)"></div>
  <div class="abs swatch" style="left:942px;background:var(--ink)"></div>
  <div class="abs swatch" style="left:993px;background:var(--paper)"></div>
  <div class="abs swatch-label" style="left:884px">#0170bb</div>
  <div class="abs swatch-label" style="left:936px">#1e1e1e</div>
  <div class="abs swatch-label" style="left:987px">#f0f1f2</div>
</header>

<main class="abs site">
  <section class="hero" role="img" aria-label="Aerial black and white photo of a busy African street market">
    <div class="nav-line"></div>
    <div class="nav-logo">ZELMOR</div>
    <div class="nav-link" style="left:205px">Home</div>
    <div class="nav-link" style="left:262px">About</div>
    <div class="nav-link" style="left:320px">Services</div>
    <div class="nav-link" style="left:386px">Team</div>
    <div class="btn-blue">Contact Us</div>
    <p class="hero-quote">ZELMOR stands out from the crowd as a consulting firm with a difference. Our dynamic team is fully dedicated to one mission: brand development within Africa.</p>
    <h1 class="hero-title">Expanding Your<br><span class="accent">Exponential</span> Growth</h1>
  </section>

  <section class="stats">
    <div class="map" role="img" aria-label="Faint outline map of Africa"></div>
    <div class="stat-num" style="left:105px">64</div>
    <div class="stat-label" style="left:107px">Happy Clients</div>
    <div class="stat-num" style="left:203px">83</div>
    <div class="stat-label" style="left:205px">Projects Done</div>
    <p class="intro">ZELMOR is a premier consulting firm that specialises in aiding global corporations &amp; emerging businesses to enter and scale within <span class="text-accent">Africa's dynamic markets</span>.</p>
  </section>

  <section class="about">
    <div class="eyebrow">About</div>
    <h2 class="section-title">Zelmor, a Leader in<br>Business Consulting</h2>
    <div class="about-card">
      <div class="photo" style="left:30px;top:29px;width:119px;height:85px;background:linear-gradient(180deg,#8fa7c4,#7a6a62)" role="img" aria-label="Photo of a crowded open-air market"></div>
      <div class="photo" style="left:177px;top:29px;width:118px;height:85px;background:linear-gradient(135deg,#1f5fa8,#7fb8ea 55%,#1a4c8a)" role="img" aria-label="Photo of glowing blue puzzle pieces"></div>
      <div class="photo" style="left:325px;top:29px;width:224px;height:188px;background:linear-gradient(145deg,#1b3d6e,#4f86c2 50%,#15325c)" role="img" aria-label="Photo of a tablet showing business analytics dashboards"></div>
      <p class="about-text">Through swift, actionable insights and innovative strategies, ZELMOR empowers clients to capitalise on <b>Africa's untapped potential</b>, thereby catering specifically to forward-thinking entities poised for exponential growth.</p>
      <div class="read-light">Read More +</div>
    </div>
  </section>

  <section class="services">
    <div class="eyebrow">Services</div>
    <h2 class="section-title">Solutions We Provide</h2>
    <div class="service" style="left:107px">
      <svg viewBox="0 0 36 36" fill="none" stroke="#1e1e1e" stroke-width="1.5"><circle cx="16" cy="20" r="12"/><circle cx="16" cy="20" r="7"/><circle cx="16" cy="20" r="2" fill="#1e1e1e"/><path d="M16 20 30 6" stroke="#0170bb"/><path d="M26 5h5v5" stroke="#0170bb"/></svg>
      <div class="service-title">Strategy Plan</div>
      <p class="service-desc">Lorem Ipsum passages, and more recently with desktop publishing software like Velo PageWriter</p>
      <div class="service-link">Read More +</div>
    </div>
    <div class="service" style="left:257px">
      <svg viewBox="0 0 36 36" fill="none" stroke="#1e1e1e" stroke-width="1.5"><path d="M14 26c0-5-6-6-6-13a8 8 0 0 1 16 0c0 7-6 8-6 13z"/><path d="M13 29h6M14 32h4"/><rect x="24" y="2" width="10" height="7" rx="1" stroke="#0170bb"/></svg>
      <div class="service-title">Innovative Solutions</div>
      <p class="service-desc">Lorem Ipsum passages, and more recently with desktop publishing software like Velo PageWriter</p>
      <div class="service-link">Read More +</div>
    </div>
    <div class="service" style="left:406px">
      <svg viewBox="0 0 36 36" fill="none" stroke="#1e1e1e" stroke-width="1.5"><rect x="4" y="3" width="24" height="24" rx="1"/><circle cx="18" cy="16" r="6"/><path d="M22 20 30 28" stroke="#0170bb"/><path d="M3 32l5-4 4 3 5-4" stroke="#0170bb"/></svg>
      <div class="service-title">Detailed Insights</div>
      <p class="service-desc">Lorem Ipsum passages, and more recently with desktop publishing software like Velo PageWriter</p>
      <div class="service-link">Read More +</div>
    </div>
    <div class="service" style="left:556px">
      <svg viewBox="0 0 36 36" fill="none" stroke="#1e1e1e" stroke-width="1.5"><rect x="3" y="28" width="4" height="5"/><rect x="10" y="24" width="4" height="9"/><rect x="17" y="20" width="4" height="13"/><rect x="24" y="14" width="4" height="19"/><path d="M4 20 28 4" stroke="#0170bb"/><path d="M23 4h5v5" stroke="#0170bb"/><path d="M3 4h6M3 7h6M3 10h4"/></svg>
      <div class="service-title">Identify Growth Pathways</div>
      <p class="service-desc">Lorem Ipsum passages, and more recently with desktop publishing software like Velo PageWriter</p>
      <div class="service-link">Read More +</div>
    </div>
  </section>

  <section class="process">
    <div class="eyebrow">The Process</div>
    <h2 class="section-title">How it Works</h2>
    <div class="step" style="left:107px">
      <div class="step-title">01 - Initiate</div><span class="step-dot"></span>
      <p class="step-desc">Lorem ipsum dolor sit amet, consectetur adipiscing elit, sed do eiusmod tempor incididunt ut labore et dolore magna</p>
    </div>
    <div class="step" style="left:321px">
      <div class="step-title">02 - Negotiate</div><span class="step-dot"></span>
      <p class="step-desc">Lorem ipsum dolor sit amet, consectetur adipiscing elit, sed do eiusmod tempor incididunt ut labore et dolore magna</p>
    </div>
    <div class="step" style="left:535px">
      <div class="step-title">03 - Validate</div><span class="step-dot"></span>
      <p class="step-desc">Lorem ipsum dolor sit amet, consectetur adipiscing elit, sed do eiusmod tempor incididunt ut labore et dolore magna</p>
    </div>
  </section>

  <section class="cta">
    <h2 class="cta-title">Initiate a Partnership</h2>
    <div class="btn-outline">Contact Us</div>
  </section>

  <footer class="footer">
    <div class="copyright">© Zelmor 2023</div>
    <div class="foot-head" style="left:403px">Stay in Touch</div>
    <div class="social" style="left:405px" aria-label="Social profile link"></div>
    <div class="social" style="left:429px" aria-label="Social profile link"></div>
    <div class="foot-head" style="left:524px">Information</div>
    <div class="foot-link" style="left:524px;top:45px">Privacy Policy</div>
    <div class="foot-link" style="left:524px;top:60px">Terms of Use</div>
    <div class="foot-head" style="left:637px">Contact</div>
    <div class="foot-link" style="left:637px;top:45px">+1 555 014 2290</div>
    <div class="foot-link" style="left:637px;top:60px">info@zelmor.example</div>
  </footer>
</main>

</body>
</html>
```